TWS Business Card Design

As a full service media and advocacy firm, we lean on years of experience in political and corporate consulting, grassroots campaigning, media placement, and video production to deliver unparalleled results. Recently we have moved into digital media and now provide this service for our clients.

I will add our two company logos to be used on the business cards. The longer logo with "sky reach studio" is our primary logo. Our secondary logo is more square one with "sky reach" and 'digital.media.campaigns" on it. We are looking for clean and modern looking business cards fitting for a digital firm.

I will also add our logos that go well with dark backgrounds.

Industry/Entity Type

Political

Contact Information for Business Card

Denton Pratchard, Director of Campaigns and Digital, 571-482-7165, denton@skyreachstudioco.com, @SkyReachStudioCo, @DentonPratchard, Facebook.com/SkyReachStudioCo

```html
<!DOCTYPE html>
<html lang="en">
<head>
<meta charset="utf-8">
<title>Sky Reach Studio – Business Cards</title>
<link href="https://fonts.googleapis.com/css2?family=Arimo:ital,wght@0,400;0,700;1,400;1,700&display=swap" rel="stylesheet">
<style>
  :root {
    --stage: #1e1e1f;
    --card: #ffffff;
    --accent: #00a1c7;
    --brand: #1d86c4;
    --ink: #2b2b2b;
    --on-accent: #ffffff;
  }
  * { box-sizing: border-box; margin: 0; padding: 0; }
  html, body {
    width: 1200px; height: 1000px; overflow: hidden;
    background: var(--stage);
    font-family: "Arimo", Arial, sans-serif;
  }
  .card {
    position: absolute;
    width: 700px; height: 400px;
    background: var(--card);
    box-shadow: 0 12px 30px rgba(0,0,0,.55);
    overflow: hidden;
  }
  /* Front face */
  .card--front { left: 440px; top: 90px; display: flex; align-items: center; justify-content: center; }
  .wordmark { display: flex; align-items: center; gap: 14px; }
  .wordmark__dot { width: 20px; height: 20px; border-radius: 50%; background: var(--brand); flex: none; }
  .wordmark__name {
    font-weight: 700; font-size: 52px; color: var(--brand);
    letter-spacing: 1px; text-transform: uppercase; white-space: nowrap;
  }
  /* Back face */
  .card--back { left: 60px; top: 530px; }
  .card__band { position: absolute; inset: 0; width: 100%; height: 100%; }
  .identity { position: absolute; left: 38px; top: 110px; white-space: nowrap; }
  .identity__name { font-weight: 700; font-style: italic; font-size: 24px; color: var(--accent); }
  .identity__title { margin-top: 4px; font-style: italic; font-size: 18px; color: var(--ink); }
  .secondary-mark {
    position: absolute; left: 38px; top: 262px;
    display: flex; align-items: center; gap: 12px; white-space: nowrap;
  }
  .secondary-mark__square { width: 18px; height: 18px; background: var(--brand); flex: none; }
  .secondary-mark__name { font-weight: 700; font-size: 42px; color: var(--brand); text-transform: uppercase; }
  .contact {
    position: absolute; left: 428px; top: 108px;
    color: var(--on-accent); font-size: 15px; line-height: 1.75; white-space: nowrap;
  }
  .social { position: absolute; left: 392px; top: 236px; list-style: none; color: var(--on-accent); font-size: 18px; white-space: nowrap; }
  .social li { display: flex; align-items: center; gap: 12px; height: 36px; }
  .social__icon { width: 22px; height: 22px; border-radius: 50%; background: var(--on-accent); flex: none; }
</style>
</head>
<body>
  <section class="card card--front" aria-label="Card front">
    <div class="wordmark">
      <span class="wordmark__dot"></span>
      <span class="wordmark__name">Sky Reach Studio</span>
    </div>
  </section>

  <section class="card card--back" aria-label="Card back">
    <svg class="card__band" viewBox="0 0 700 400" preserveAspectRatio="none" aria-hidden="true">
      <polygon points="445,0 700,0 700,400 345,400" fill="var(--accent)"/>
    </svg>

    <div class="identity">
      <p class="identity__name">Denton Pratchard</p>
      <p class="identity__title">Director of Campaigns and Digital</p>
    </div>

    <div class="secondary-mark">
      <span class="secondary-mark__square"></span>
      <span class="secondary-mark__name">Sky Reach</span>
    </div>

    <div class="contact">
      <p>p : 571-482-7165</p>
      <p>e : denton@skyreachstudioco.com</p>
    </div>

    <ul class="social">
      <li><span class="social__icon"></span>@DentonPratchard</li>
      <li><span class="social__icon"></span>@SkyReachStudioCo</li>
      <li><span class="social__icon"></span>/SkyReachStudioCo</li>
    </ul>
  </section>
</body>
</html>
```